Modern Business Card for Speech Therapy Practice
Clear Sound Harbor LLC
Bright & Fun-filled
Odile Varnet, M.A., CCC-SLP
827 Quarry Ln.
Moonachie, NJ 07391
Odile.Varnet@mailbrook.net
www.ClearSoundHarbor.net
NJ Lic: 58KT00394817

```html
<!DOCTYPE html>
<html lang="en">
<head>
<meta charset="utf-8">
<title>Clear Sound Harbor – Business Card Set</title>
<link href="https://fonts.googleapis.com/css2?family=Open+Sans:wght@400;600;700&family=Cinzel:wght@400&display=swap" rel="stylesheet">
<style>
  :root {
    --backdrop: #3a2a22;
    --card: #ffffff;
    --green: #7cbf2e;
    --orange: #f07a1e;
    --navy: #1f3a5c;
    --ink: #3b3b3b;
    --label: #f2ece6;
  }
  * { margin: 0; padding: 0; box-sizing: border-box; }
  html, body { width: 1200px; height: 825px; overflow: hidden; }
  body {
    background: var(--backdrop);
    font-family: "Open Sans", Arial, sans-serif;
    position: relative;
  }
  .card {
    position: absolute;
    width: 571px;
    height: 324px;
    background: var(--card);
    overflow: hidden;
    box-shadow: 0 3px 8px rgba(0,0,0,.45);
  }
  .card svg.bands { position: absolute; inset: 0; width: 100%; height: 100%; }
  .front-1 { left: 19px; top: 19px; }
  .front-2 { left: 607px; top: 19px; }
  .back-1 { left: 19px; top: 408px; }
  .back-2 { left: 607px; top: 408px; }

  .label {
    position: absolute;
    font-family: "Cinzel", Georgia, serif;
    font-size: 19px;
    color: var(--label);
    width: 571px;
    text-align: center;
  }
  .label-top { top: 362px; }
  .label-bottom { top: 752px; }
  .label-left { left: 19px; }
  .label-right { left: 607px; }

  .brand {
    position: absolute;
    display: flex;
    align-items: center;
    gap: 8px;
    font-weight: 700;
    color: var(--navy);
    white-space: nowrap;
  }
  .brand-dot { width: 14px; height: 14px; border-radius: 50%; background: var(--orange); flex: none; }
  .brand-small { font-size: 20px; }
  .brand-large { font-size: 34px; }
  .brand-front-1 { left: 34px; top: 118px; }
  .brand-front-2 { right: 30px; top: 72px; }
  .brand-back-1 { left: 0; width: 530px; justify-content: center; top: 140px; }
  .brand-back-2 { left: 41px; right: 0; justify-content: center; top: 140px; }

  .holder-name {
    position: absolute;
    font-size: 12.5px;
    color: var(--green);
    font-weight: 600;
    white-space: nowrap;
  }
  .contact {
    position: absolute;
    font-size: 12px;
    line-height: 15px;
    color: var(--ink);
    white-space: nowrap;
  }
  .contact .gap { height: 12px; }
  .bullet {
    display: inline-block;
    width: 8px; height: 8px; border-radius: 50%;
    margin-right: 4px;
  }
  .bullet-orange { background: var(--orange); }
  .bullet-green { background: var(--green); }
  .web-line {
    position: absolute;
    bottom: 44px;
    text-align: center;
    font-size: 12px;
  }
  .web-green { color: var(--green); left: 0; width: 530px; }
  .web-orange { color: var(--orange); left: 41px; width: 530px; }
</style>
</head>
<body>

  <section class="card front-1">
    <svg class="bands" viewBox="0 0 571 324" aria-hidden="true">
      <line x1="300" y1="150" x2="540" y2="150" stroke="#7cbf2e" stroke-width="1.5"/>
      <polygon points="528,138 571,138 571,162 528,162 540,150" fill="#7cbf2e"/>
      <rect x="0" y="296" width="480" height="13" fill="#7cbf2e"/>
      <polygon points="480,324 571,256 571,324" fill="#f07a1e"/>
    </svg>
    <div class="brand brand-small brand-front-1"><span class="brand-dot"></span>Clear Sound Harbor</div>
    <div class="holder-name" style="left:300px; top:128px;">Odile Varnet, M.A., CCC-SLP</div>
    <div class="contact" style="left:300px; top:166px;">
      <div>NJ Lic: 58KT00394817</div>
      <div>827 Quarry Ln. Moonachie, NJ 07391</div>
      <div class="gap"></div>
      <div>201-555-0147</div>
      <div>Odile.Varnet@mailbrook.net</div>
      <div>www.ClearSoundHarbor.net</div>
    </div>
  </section>

  <section class="card front-2">
    <svg class="bands" viewBox="0 0 571 324" aria-hidden="true">
      <polygon points="0,138 26,138 38,150 26,162 0,162" fill="#f07a1e"/>
      <rect x="90" y="296" width="481" height="13" fill="#7cbf2e"/>
      <polygon points="0,256 0,324 90,324" fill="#f07a1e"/>
    </svg>
    <div class="holder-name" style="left:58px; top:128px;">Odile Varnet, M.A., CCC-SLP</div>
    <div class="contact" style="left:58px; top:166px;">
      <div>NJ Lic: 58KT00394817</div>
      <div>827 Quarry Ln. Moonachie, NJ 07391</div>
      <div class="gap"></div>
      <div><span class="bullet bullet-orange"></span>201-555-0147</div>
      <div><span class="bullet bullet-orange"></span>Odile.Varnet@mailbrook.net</div>
      <div><span class="bullet bullet-green"></span>www.ClearSoundHarbor.net</div>
    </div>
    <div class="brand brand-small brand-front-2"><span class="brand-dot"></span>Clear Sound Harbor</div>
  </section>

  <section class="card back-1">
    <svg class="bands" viewBox="0 0 571 324" aria-hidden="true">
      <rect x="530" y="0" width="18" height="324" fill="#f07a1e"/>
      <rect x="548" y="0" width="23" height="324" fill="#7cbf2e"/>
    </svg>
    <div class="brand brand-large brand-back-1"><span class="brand-dot"></span>Clear Sound Harbor</div>
    <div class="web-line web-green">www.ClearSoundHarbor.net</div>
  </section>

  <section class="card back-2">
    <svg class="bands" viewBox="0 0 571 324" aria-hidden="true">
      <rect x="0" y="0" width="23" height="324" fill="#7cbf2e"/>
      <rect x="23" y="0" width="18" height="324" fill="#f07a1e"/>
    </svg>
    <div class="brand brand-small brand-back-2"><span class="brand-dot"></span>Clear Sound Harbor</div>
    <div class="web-line web-orange">www.ClearSoundHarbor.net</div>
  </section>

  <div class="label label-top label-left">Front-1</div>
  <div class="label label-top label-right">Front-2</div>
  <div class="label label-bottom label-left">Back-1</div>
  <div class="label label-bottom label-right">Back-2</div>

</body>
</html>
```